Single Splash Web Page as Long Term Placeholder

I registered the url PebbleAndPine.com. This is the name of a business I will be starting several years down the road. It will be a coffee (drips) and ice cream (dips) store located in a beach town somewhere on the east coast of the US, probably in the Outer Banks of NC. I need a single page that will have the name of the business and the text:

Coming eventually to a beach near you!

The page should somehow reflect the beach environment.

```html
<!DOCTYPE html>
<html lang="en">
<head>
<meta charset="utf-8">
<title>Pebble &amp; Pine — Ice Cream . Coffee . More</title>
<link rel="stylesheet" href="https://fonts.googleapis.com/css2?family=Bree+Serif&display=swap">
<style>
  :root {
    --sky-light: #f3f2d8;
    --sky-gold: #e6df86;
    --horizon: #cfc06a;
    --sand: #b8a46c;
    --sand-deep: #8c7848;
    --shade: rgba(40, 44, 24, 0.55);
    --navy: #0f2a4a;
    --band: #ffffff;
    --band-text: #1a1a1a;
    --accent: #7a1250;
    --frame: #eef2ec;
    --rule: #ffffff;
  }
  * { margin: 0; padding: 0; box-sizing: border-box; }
  html, body { width: 1200px; height: 577px; overflow: hidden; }
  body { font-family: "Bree Serif", Georgia, serif; background: #ffffff; }

  .splash { position: relative; width: 1200px; height: 577px; overflow: hidden; }

  .beach-scene {
    position: absolute; inset: 0;
    background:
      linear-gradient(90deg, rgba(0,0,0,0) 0%, rgba(0,0,0,0) 50%, var(--shade) 100%),
      linear-gradient(180deg, var(--sky-light) 0%, #eeecc0 30%, var(--sky-gold) 50%, var(--horizon) 63%, var(--sand) 76%, var(--sand-deep) 100%);
  }

  .polaroid { position: absolute; background: var(--frame); box-shadow: 0 2px 8px rgba(0,0,0,.25); }
  .polaroid .snapshot { position: absolute; }
  .polaroid--cones   { left: 33px; top: -20px; width: 179px; height: 152px; }
  .polaroid--cones .snapshot { left: 13px; top: 20px; width: 155px; height: 83px; background: linear-gradient(135deg, #2f6b56, #5a3a22); }
  .polaroid--cup     { left: 77px; top: 72px; width: 180px; height: 218px; }
  .polaroid--cup .snapshot { left: 12px; top: 11px; width: 158px; height: 158px; background: linear-gradient(180deg, #f4fbfb 0%, #8fd3d6 55%, #3a2a20 100%); }
  .polaroid--waffle  { left: 4px; top: 213px; width: 204px; height: 170px; }
  .polaroid--waffle .snapshot { left: 14px; top: 14px; width: 178px; height: 138px; background: linear-gradient(135deg, #2e7a52, #b8a577 55%, #3a2616); }
  .polaroid--edge    { left: 4px; top: 400px; width: 86px; height: 57px; }
  .polaroid--iced    { left: 90px; top: 400px; width: 205px; height: 190px; }
  .polaroid--iced .snapshot { left: 12px; top: 13px; width: 180px; height: 144px; background: linear-gradient(180deg, #e8ece4 0%, #6b3a22 55%, #2c2a24 100%); }

  .masthead { position: absolute; left: 300px; top: 100px; width: 600px; text-align: center; }
  .masthead__name {
    font-size: 75px; font-weight: 400; line-height: 1; color: var(--navy);
  }
  .masthead__tagline {
    position: relative; margin-top: 26px;
    font-size: 26px; line-height: 34px; letter-spacing: 3.8px; color: var(--navy);
  }
  .masthead__rule { position: absolute; top: 16px; }

  .announcement {
    position: absolute; left: 0; top: 366px; width: 1200px; height: 47px;
    background: var(--band);
    display: flex; align-items: center; justify-content: center;
    font-size: 20.5px; color: var(--band-text);
  }
  .announcement__you { color: var(--accent); margin-left: 6px; }
</style>
</head>
<body>
<main class="splash">
  <div class="beach-scene" role="img" aria-label="Sunset over a palm-lined beach with golden sky and footprinted sand"></div>

  <div class="polaroid polaroid--cones"><div class="snapshot" role="img" aria-label="Chocolate-dipped ice cream cones with sprinkles"></div></div>
  <div class="polaroid polaroid--cup"><div class="snapshot" role="img" aria-label="Coffee splashing from a turquoise cup with coffee beans"></div></div>
  <div class="polaroid polaroid--waffle"><div class="snapshot" role="img" aria-label="Waffle cone with chocolate ice cream on crumpled paper"></div></div>
  <div class="polaroid polaroid--edge"></div>
  <div class="polaroid polaroid--iced"><div class="snapshot" role="img" aria-label="Iced coffee in a glass beside a jar of cream"></div></div>

  <header class="masthead">
    <h1 class="masthead__name">Pebble &amp; Pine</h1>
    <p class="masthead__tagline">
      <svg class="masthead__rule" style="left:23px" width="55" height="2" aria-hidden="true"><line x1="0" y1="1" x2="55" y2="1" stroke="var(--rule)" stroke-width="1"/></svg>
      ICE CREAM . COFFEE . MORE
      <svg class="masthead__rule" style="left:527px" width="45" height="2" aria-hidden="true"><line x1="0" y1="1" x2="45" y2="1" stroke="var(--rule)" stroke-width="1"/></svg>
    </p>
  </header>

  <p class="announcement">Eventually Coming to a Beach near<span class="announcement__you">You !</span></p>
</main>
</body>
</html>
```